Design a few pages of a luxury magazine for the Prestige Aubergerie Lyon

We need a luxury design for our magazine. See the inDesign pages of the current version attached (zip).

Please work primarily on the first double page (Inventez le luxe de demain) that contains only one photo with legend, a title and the text both in French and English. It must be made clear that the text is the same in two different languages (it is not clear enough here).

You can also work on the other two double pages selected. Feedback will be provided and the 10 best pages will be submitted to a vote at the end of the project timespan.

The most important is a classy and luxury design, this will be printed on expensive paper.

See the full brochure here: https://www.prestigeaubergerie.com/brochure/#page=4

Target Market(s)

Students and parents

Industry/Entity Type

Education

Colors

Designer to choose colors to be used in the design.

Requirements
Must have
• Luxury magazine layout, see:
• https://www.findwerk.com/search?q=luxury+magazine+layout&client=safari&rls=en&source=lnms&tbm=isch&sa=X&ved=0ahUKEwitoIDmit7fAhUVShUIHXC2Cd4Q_AUIDigB&biw=1010&bih=702
Nice to have
• The color of the cover that should be used for blue and grey is #393d49.
• Our font for serif titles (from the logo) is Adobe TRAJAN.
Should not have
• flashy colors

```html
<!DOCTYPE html>
<html lang="fr">
<head>
<meta charset="utf-8">
<title>Prestige Aubergerie Lyon — Inventez le luxe de demain</title>
<link rel="stylesheet" href="https://fonts.googleapis.com/css2?family=Cinzel:wght@400&family=Fira+Sans+Condensed:wght@300;400&family=Fira+Sans:wght@300;400&family=Playfair+Display:wght@900&display=swap">
<style>
  :root{
    --backdrop:#dcdddf;
    --navy:#2e3442;
    --ink:#262c3a;
    --gold:#c9a277;
    --gold-text:#c49a6c;
    --paper:#ffffff;
    --logo-grey:#c5c8cf;
    --body:#4a4d55;
    --photo-dark:#2a2620;
    --photo-warm:#8a6a3c;
  }
  *{margin:0;padding:0;box-sizing:border-box}
  html,body{width:1200px;height:1000px;overflow:hidden;background:var(--backdrop)}
  .canvas{position:relative;width:1200px;height:1000px}

  .cover{position:absolute;left:36px;top:34px;width:462px;height:589px;background:var(--navy)}
  .cover-name{position:absolute;left:227px;top:268px;font-family:"Cinzel",serif;font-size:15px;line-height:19px;color:var(--logo-grey);letter-spacing:.3px}

  .spread{position:absolute;left:226px;top:369px;width:926px;height:589px;background:var(--paper)}
  .spine{position:absolute;left:463px;top:0;width:1px;height:100%;background:#e6e6e6}

  .photo{position:absolute;left:0;top:0;width:462px;height:358px;
    background:radial-gradient(ellipse at 50% 35%, var(--photo-warm) 0%, #5a4a33 35%, var(--photo-dark) 80%)}
  .section-tag{position:absolute;left:132px;top:0;width:198px;height:37px;background:var(--gold);
    font-family:"Cinzel",serif;font-size:10.5px;letter-spacing:1.6px;color:var(--paper);
    display:flex;align-items:center;justify-content:center;text-transform:uppercase;white-space:nowrap}

  .title-band{position:absolute;left:132px;top:339px;width:198px;height:38px;background:var(--gold);
    font-family:"Playfair Display",serif;font-weight:900;font-size:40px;line-height:34px;color:var(--paper);
    text-align:center;letter-spacing:.5px;white-space:nowrap}
  .title-le{position:absolute;left:74px;top:384px;font-family:"Fira Sans Condensed",sans-serif;font-weight:300;font-size:42px;line-height:42px;color:var(--ink)}
  .title-luxe{position:absolute;left:126px;top:372px;width:210px;text-align:center;font-family:"Fira Sans Condensed",sans-serif;font-weight:300;font-size:100px;line-height:92px;color:var(--ink);letter-spacing:3px;white-space:nowrap}
  .title-demain{position:absolute;left:122px;top:456px;width:218px;text-align:center;font-family:"Fira Sans Condensed",sans-serif;font-weight:300;font-size:35px;line-height:34px;color:var(--ink);letter-spacing:3.5px;white-space:nowrap}
  .title-rule{position:absolute;left:132px;top:497px;width:198px;height:1px;background:var(--gold)}
  .title-english{position:absolute;left:96px;top:504px;width:270px;text-align:center;font-family:"Fira Sans",sans-serif;font-weight:300;font-size:10px;line-height:17px;letter-spacing:1.9px;color:var(--gold-text);text-transform:uppercase;white-space:nowrap}

  .folio{position:absolute;top:556px;font-family:"Fira Sans",sans-serif;font-size:6px;color:var(--body);letter-spacing:1px}
  .folio-left{left:227px}
  .folio-right{left:690px}

  .body-col{position:absolute;top:220px;font-family:"Fira Sans",sans-serif;font-size:6.3px;line-height:8.1px;color:var(--body);text-align:justify;hyphens:auto}
  .body-col p{margin-bottom:6px}
  .col-fr{left:490px;width:187px}
  .col-en{left:702px;width:199px}
</style>
</head>
<body>
<div class="canvas">

  <section class="cover">
    <div class="cover-name">Prestige<br>Aubergerie<br>Lyon</div>
  </section>

  <section class="spread">
    <div class="spine"></div>

    <div class="photo" role="img" aria-label="Photographie de l'équipe de direction, quatre personnes en costume autour d'un canapé de velours vert dans un salon d'hôtel éclairé"></div>
    <div class="section-tag">À la Prestige Aubergerie</div>

    <div class="title-band">inventez</div>
    <div class="title-le">LE</div>
    <div class="title-luxe">LUXE</div>
    <div class="title-demain">DE DEMAIN</div>
    <div class="title-rule"></div>
    <div class="title-english">Invent tomorrow's luxuries<br>at the Prestige Aubergerie</div>

    <div class="folio folio-left">[ 2 ]</div>
    <div class="folio folio-right">[ 3 ]</div>

    <div class="body-col col-fr" lang="fr">
      <p>Depuis sa création il y a 30 ans, notre école garde le même objectif : que chaque étudiant acquière les compétences et développe les talents essentiels pour briller dans l'univers du luxe. Première école dédiée à l'hôtellerie de luxe, la Prestige Aubergerie délivre un Bachelor et un Master of Science in International Tourism and Hospitality Management, deux grades universitaires anglais.</p>
      <p>Cette combinaison du luxe à la française et du management anglo-saxon donne toutes les clés à nos étudiants pour s'assurer une place privilégiée dans l'univers du luxe en France et à l'international.</p>
      <p>Grâce à l'excellence académique de nos programmes, la dimension internationale de nos formations et l'immersion professionnelle à travers des stages dans les plus prestigieux hôtels du monde, tous nos diplômés sont assurés de faire carrière dans le secteur de leur choix à un poste stratégique. La moitié d'entre eux signent un CDI avant même la fin de leur dernier stage.</p>
    </div>

    <div class="body-col col-en" lang="en">
      <p>Since its foundation 30 years ago, our school has had only one objective: that each student acquires the skills and develops the essential talents they require to shine within the luxury sector. The Prestige Aubergerie is the first Higher Education establishment dedicated to luxury hotel training: we offer a Bachelor's and a Master's degree in International Tourism and Hospitality Management.</p>
      <p>This combination of French-style luxury and Anglo-Saxon management gives our students the key elements they need to ensure a privileged position within the luxury industry both in France and internationally.</p>
      <p>The academic excellence of our programmes, the international dimension of our training and our professional work placements at the most prestigious hotels in the world all ensure that our graduates are certain to secure a career in a strategic role in the luxury sector. Half of our students sign a permanent contract before they even finish their final work placement.</p>
    </div>
  </section>

</div>
</body>
</html>
```